Letterhead Design Project

Consulting Company , we want a letterhead incorporating both the picture provided and the logo provided. The font name is monotype corsiva.
Target Market(s)
Dentist
Industry/Entity Type
Consulting
Font styles to use
Other font styles liked:
- monotype corsiva

Colors
0455a3
Requirements
Must have
- the logo, the picture (see attached), the website name, the email. and the phone numbers.
- Website: www.trquillarisadvisory.solutions
- Email: will be provided to the winner, please use placeholder
- Phone numbers:
- Petra Hallum 5829017763
- Owen Vrastik 6148250397

Nice to have
- a swoop or wave across the bottom. a line up the side. I don't know guys. design something unique and professional.

Should not have
- arrows pointing off the logo or anywhere. no arrows. our logo altered in anyway. no broken circles. no variences in blue. we like our logo the way it is. the font is monotype corsiva

```html
<!DOCTYPE html>
<html lang="en">
<head>
<meta charset="utf-8">
<title>Trquillaris Advisory – Letterhead</title>
<link href="https://fonts.googleapis.com/css2?family=Cormorant+Garamond:ital,wght@1,500;1,600&family=Source+Sans+3:wght@400;700&display=swap" rel="stylesheet">
<style>
  :root {
    --brand-blue: #0455a3;
    --ink: #1a1a1a;
    --body-grey: #555555;
    --paper: #ffffff;
    --backdrop: #4a4a4a;
    --photo-tone: #c9c9c9;
  }
  * { margin: 0; padding: 0; box-sizing: border-box; }
  html, body { width: 999px; height: 1200px; overflow: hidden; background: var(--backdrop); }
  .canvas { position: relative; width: 999px; height: 1200px; }
  .sheet {
    position: absolute; left: 66px; top: 39px; width: 867px; height: 1122px;
    background: var(--paper); overflow: hidden;
  }
  .header-rules { position: absolute; left: 0; top: 0; }
  .brand-ring {
    position: absolute; left: 62px; top: 56px; width: 90px; height: 90px;
    border: 5px solid var(--brand-blue); border-radius: 50%; background: var(--paper);
  }
  .script { font-family: "Cormorant Garamond", "Times New Roman", serif; font-style: italic; }
  .company-name {
    position: absolute; left: 166px; top: 90px; font-size: 24px; font-weight: 500;
    color: var(--brand-blue); white-space: nowrap;
  }
  .address {
    position: absolute; left: 164px; top: 119px; font-size: 13px; line-height: 19px;
    font-weight: 600; color: var(--ink);
  }
  .letter { position: absolute; left: 74px; top: 264px; width: 720px; font-family: "Source Sans 3", Arial, sans-serif; color: var(--body-grey); }
  .letter-title { font-size: 22px; font-weight: 700; line-height: 30px; }
  .letter-subtitle { font-size: 15px; line-height: 21px; margin-top: 6px; }
  .letter-body { margin-top: 37px; }
  .letter-body p { font-size: 15px; line-height: 20.3px; text-align: justify; margin-bottom: 20px; }
  .signature-name {
    position: absolute; left: 446px; top: 966px; font-size: 36px; font-weight: 500;
    color: var(--brand-blue); white-space: nowrap;
  }
  .signature-phone {
    position: absolute; left: 450px; top: 1010px; font-size: 22px; font-weight: 500;
    color: var(--ink);
  }
  .portrait {
    position: absolute; left: 648px; top: 830px; width: 146px; height: 208px;
    background: linear-gradient(180deg, #e6e6e6 0%, var(--photo-tone) 55%, #6f6f6f 100%);
  }
  .footer-rule { position: absolute; left: 0; top: 1055px; width: 867px; height: 5px; background: var(--brand-blue); }
  .footer-line {
    position: absolute; top: 1067px; font-size: 15px; font-weight: 600; color: var(--ink);
  }
  .footer-email { left: 74px; }
  .footer-web { right: 73px; }
</style>
</head>
<body>
<div class="canvas">
  <div class="sheet">
    <svg class="header-rules" width="867" height="90" viewBox="0 0 867 90" aria-hidden="true">
      <polygon points="134,58 387,58 391,63 134,63" fill="#0455a3"/>
      <polygon points="134,70 572,70 577,75 134,75" fill="#0455a3"/>
      <polygon points="134,82 862,82 867,87 134,87" fill="#0455a3"/>
    </svg>
    <div class="brand-ring"></div>
    <div class="company-name script">Trquillaris Advisory, LLC</div>
    <div class="address script">418 Larkspur Lane<br>Alder Bend, Kentucky 40398</div>

    <div class="letter">
      <h1 class="letter-title">Lorem ipsum dolor sit amet</h1>
      <p class="letter-subtitle">Lorem ipsum dolor sit amet,<br>consectetur adipiscing elit.</p>
      <div class="letter-body">
        <p>Lorem ipsum dolor sit amet, consectetur adipiscing elit. Integer eu odio mattis, pulvinar turpis quis, faucibus nisl. Proin feugiat, erat vitae cursus pharetra, enim est semper ligula, in malesuada orci nisl et diam. Etiam elementum metus ac fringilla vulputate. Etiam mattis ligula sed ante mollis bibendum. Orci varius natoque penatibus et magnis dis parturient montes, nascetur ridiculus mus.</p>
        <p>Ut nibh augue, blandit ac orci ac, rutrum congue enim. Suspendisse gravida vulputate felis, quis interdum orci tincidunt quis. Praesent imperdiet maximus neque. Mauris ut dui enim. Nullam at efficitur elit. Donec ante ipsum, fermentum at lectus vel, blandit vulputate ante. Proin luctus suscipit diam id vestibulum. Morbi malesuada id mauris eget ullamcorper.</p>
        <p>Donec varius orci purus, vitae aliquam libero volutpat id. Integer sed imperdiet libero. Aliquam accumsan, risus sit amet ornare consectetur, turpis felis dictum justo, non rhoncus mauris dui sed velit. Pellentesque habitant morbi tristique senectus et netus et malesuada fames ac turpis egestas. Pellentesque tincidunt vitae ligula nec imperdiet. Donec sed congue enim. Nullam elementum faucibus nulla nec vestibulum. Sed at tempor ligula. In quis vulputate nunc. Integer at gravida lacus, ac tristique risus. Sed at vulputate nulla.</p>
        <p>Praesent blandit nunc eu efficitur commodo. In tempor nisi ex, vel venenatis ante vestibulum a. Duis vestibulum nibh a erat sagittis, nec euismod lorem varius. Nam ultricies turpis sed justo sollicitudin volutpat. Morbi sed mollis eros. Sed quis tortor id enim vehicula porttitor. Curabitur non aliquam ex. Phasellus dignissim fermentum elit, at finibus ligula mattis eget.</p>
      </div>
    </div>

    <div class="signature-name script">Petra Hallum</div>
    <div class="signature-phone script">5829017763</div>
    <div class="portrait" role="img" aria-label="Black and white portrait photograph of Petra Hallum"></div>

    <div class="footer-rule"></div>
    <div class="footer-line footer-email script">info@trquillarisadvisory.solutions</div>
    <div class="footer-line footer-web script">www.trquillarisadvisory.solutions</div>
  </div>
</div>
</body>
</html>
```